Interpretive Signs x 2

We would like 2 x Aboriginal themed signs. Design to be relaxed, contemporary, clean, fresh, inspiring natural Aboriginal themes tying in traditional elements.

Sign 1: Meeting Place - A1 sized (or A0 if better for design/layout)
Sign 2: The Six Seasons - A2 (or A1 if better for design/layout)
See file 12 for proposed layout (this is just an idea I had - it doesn't have to be like this!)

Requirements
Must have
• Use the symbols provided. Primarily use images provided. See our website www.tallowbrookfarm.com.au for our branding style. Stock images for fire etc ok as long as they do not show a location. If using any stock images of trees etc, they must be native to South West WA (ie Karri, Jarrah, Marri).
Nice to have
• Fonts preferred to be "Quiet River Run" as attached if this works with design - but not essential.

Perhaps use our logo colors where possible/appropriate - not essential!
Should not have
• Anything that breaches Aboriginal copyright or IP. The design elements must be generic with an Aboriginal theme and not be specifically representative of other Aboriginal people from other regions.

Any depictions of nature or Aboriginal people must be relevant to the South West of Western Australia - and not show nature or culture which does not belong here.

No pictures of trees or landscapes (mountains etc) which are clearly not from here (we have no mountains - just forest).

```html
<!DOCTYPE html>
<html lang="en">
<head>
<meta charset="utf-8">
<title>The Wardandi Six Seasons</title>
<link rel="stylesheet" href="https://fonts.googleapis.com/css2?family=Big+Shoulders+Display:wght@200&family=EB+Garamond:wght@700&family=Arimo:wght@400;700&display=swap">
<style>
  :root{
    --frame:#6b3a2a;
    --heading:#7a2e22;
    --body:#4a2a22;
    --leaf:#7fa444;
    --footer:#86a84a;
    --birak:#eef1a6;
    --kambarang:#f3b68c;
    --bunuru:#a9d6b3;
    --djilba:#f1a5a7;
    --djeran:#b3b1ee;
    --makuru:#cbb0d8;
    --wheel:#f7f1da;
    --core:#fbf5c8;
  }
  *{margin:0;padding:0;box-sizing:border-box}
  html,body{width:848px;height:1200px;overflow:hidden}
  body{position:relative;font-family:"EB Garamond",Georgia,serif;color:var(--body)}
  .backdrop{position:absolute;inset:0;background:linear-gradient(160deg,#dfe4e6,#eef0ee 45%,#d9dfe0)}
  .sign{position:absolute;left:30px;top:28px;width:800px;height:1150px;border:3px solid var(--frame);background:#fff;overflow:hidden}
  .header{position:absolute;left:0;top:0;width:100%;height:106px;background:#fff}
  .brand{position:absolute;left:10px;top:12px;width:130px;text-align:center}
  .brand-dot{display:block;width:46px;height:46px;border-radius:50%;background:var(--leaf);margin:0 auto 8px}
  .brand-name{font-family:"EB Garamond",Georgia,serif;font-weight:700;font-size:14px;color:var(--leaf);letter-spacing:.5px}
  .title{position:absolute;left:176px;top:14px;font-family:"Big Shoulders Display",Impact,sans-serif;font-weight:200;font-size:66px;letter-spacing:.5px;color:var(--frame);line-height:1;white-space:nowrap}
  .tree-art{position:absolute;right:24px;top:10px;width:88px;height:88px;border-radius:50%;background:radial-gradient(circle,#9cc65a,#6e9a36 70%,#fff 71%)}
  .rule{position:absolute;left:0;top:106px;width:100%;height:13px;background:var(--leaf)}
  .wheel-art{position:absolute;left:0;top:0}
  .season{position:absolute;font-weight:700}
  .season .months{font-size:16px;color:var(--heading);letter-spacing:.3px;line-height:26px}
  .season .name{font-size:27px;color:var(--heading);letter-spacing:.5px;line-height:34px;margin:2px 0 5px}
  .season p{font-size:15px;line-height:23px;color:var(--body)}
  .birak{left:230px;top:133px;width:340px;text-align:center}
  .birak .name{margin:3px 0 3px}
  .birak p{line-height:24px}
  .kambarang{left:22px;top:211px}
  .bunuru{right:32px;top:249px;text-align:right}
  .djilba{left:22px;top:674px}
  .djilba p{line-height:23.5px}
  .djeran{right:32px;top:646px;text-align:right}
  .djeran p{line-height:22.6px}
  .makuru{left:180px;top:834px;width:440px;text-align:center}
  .makuru p{line-height:22.7px}
  .credit{position:absolute;left:0;width:100%;top:1026px;text-align:center;font-family:Arimo,Arial,sans-serif;font-size:9px;line-height:11px;color:#333}
  .footer{position:absolute;left:0;top:1041px;width:100%;height:103px}
  .photo-left{position:absolute;left:0;top:0;width:170px;height:103px;background:linear-gradient(160deg,#cfe0c8,#6f8f5a 60%,#3e5a33)}
  .photo-right{position:absolute;right:0;top:0;width:172px;height:103px;background:linear-gradient(200deg,#3f5b2a,#8c4a2a 55%,#c76a3a)}
  .contact{position:absolute;left:170px;top:0;width:452px;height:103px;background:var(--footer);text-align:center;font-family:Arimo,Arial,sans-serif;font-size:13px;line-height:19px;color:#222;padding-top:14px;font-style:normal}
  .contact b{font-weight:700}
  .wheel-text{font-family:Arimo,Arial,sans-serif;font-weight:700;fill:var(--frame)}
</style>
</head>
<body>
<div class="backdrop" role="img" aria-label="Soft faded photograph of forest trees behind the sign"></div>

<main class="sign">
  <svg class="wheel-art" width="800" height="1150" viewBox="30 28 800 1150">
    <defs>
      <path id="ringMonthB" d="M430,802 A212,212 0 1 1 430,378 A212,212 0 1 1 430,802"/>
      <path id="ringMonthT" d="M430,378 A212,212 0 1 1 430,802 A212,212 0 1 1 430,378"/>
      <path id="ringSeasonB" d="M430,757 A167,167 0 1 1 430,423 A167,167 0 1 1 430,757"/>
      <path id="ringSeasonT" d="M430,423 A167,167 0 1 1 430,757 A167,167 0 1 1 430,423"/>
      <path id="ringInnerB" d="M430,711 A121,121 0 1 1 430,469 A121,121 0 1 1 430,711"/>
      <path id="ringInnerT" d="M430,469 A121,121 0 1 1 430,711 A121,121 0 1 1 430,469"/>
    </defs>
    <g class="season-fields">
      <polygon points="150,147 700,147 430,600" fill="var(--birak)"/>
      <polygon points="30,147 150,147 430,600 30,605" fill="var(--kambarang)"/>
      <polygon points="700,147 830,147 830,605 430,600" fill="var(--bunuru)"/>
      <polygon points="30,605 430,600 160,1072 30,1072" fill="var(--djilba)"/>
      <polygon points="830,605 830,1072 705,1072 430,600" fill="var(--djeran)"/>
      <polygon points="160,1072 705,1072 430,600" fill="var(--makuru)"/>
    </g>
    <g class="calendar-wheel" stroke="var(--frame)" fill="none" stroke-width="1.6">
      <circle cx="430" cy="590" r="240" fill="var(--wheel)"/>
      <circle cx="430" cy="590" r="198"/>
      <circle cx="430" cy="590" r="150"/>
      <circle cx="430" cy="590" r="105" fill="var(--core)" role="img" aria-label="Map of Australia with the south-west region highlighted"/>
      <path d="M430,392L430,350M529,418.5L550,382.2M601.5,491L637.8,470M628,590L670,590M601.5,689L637.8,710M529,761.5L550,797.8M430,788L430,830M331,761.5L310,797.8M258.5,689L222.2,710M232,590L190,590M258.5,491L222.2,470M331,418.5L310,382.2"/>
      <path d="M505,460.1L529,418.5M580,590L628,590M505,719.9L529,761.5M355,719.9L331,761.5M280,590L232,590M355,460.1L331,418.5"/>
      <path d="M504.2,515.8L536.1,483.9M504.2,664.2L536.1,696.1M355.8,664.2L323.9,696.1M355.8,515.8L323.9,483.9"/>
    </g>
    <g class="wheel-text" font-size="15" text-anchor="middle" letter-spacing="1">
      <text><textPath href="#ringMonthB" startOffset="54.17%">JANUARY</textPath></text>
      <text><textPath href="#ringMonthB" startOffset="62.5%">FEBRUARY</textPath></text>
      <text><textPath href="#ringMonthB" startOffset="70.83%">MARCH</textPath></text>
      <text><textPath href="#ringMonthB" startOffset="79.17%">APRIL</textPath></text>
      <text><textPath href="#ringMonthB" startOffset="87.5%">MAY</textPath></text>
      <text><textPath href="#ringMonthT" startOffset="45.83%">JUNE</textPath></text>
      <text><textPath href="#ringMonthT" startOffset="54.17%">JULY</textPath></text>
      <text><textPath href="#ringMonthB" startOffset="12.5%">AUGUST</textPath></text>
      <text><textPath href="#ringMonthB" startOffset="20.83%">SEPTEMBER</textPath></text>
      <text><textPath href="#ringMonthB" startOffset="29.17%">OCTOBER</textPath></text>
      <text><textPath href="#ringMonthB" startOffset="37.5%">NOVEMBER</textPath></text>
      <text><textPath href="#ringMonthB" startOffset="45.83%">DECEMBER</textPath></text>
    </g>
    <g class="wheel-text" font-size="15" text-anchor="middle" letter-spacing="1">
      <text><textPath href="#ringSeasonB" startOffset="50%">BIRAK</textPath></text>
      <text><textPath href="#ringSeasonB" startOffset="66.67%">BUNURU</textPath></text>
      <text><textPath href="#ringSeasonB" startOffset="83.33%">DJERAN</textPath></text>
      <text><textPath href="#ringSeasonT" startOffset="50%">MAKURU</textPath></text>
      <text><textPath href="#ringSeasonB" startOffset="16.67%">DJILBA</textPath></text>
      <text><textPath href="#ringSeasonB" startOffset="33.33%">KAMBARANG</textPath></text>
    </g>
    <g class="wheel-text" font-size="14" text-anchor="middle" letter-spacing="1">
      <text><textPath href="#ringInnerB" startOffset="55.5%">SUMMER</textPath></text>
      <text><textPath href="#ringInnerB" startOffset="78%">AUTUMN</textPath></text>
      <text><textPath href="#ringInnerT" startOffset="50%">WINTER</textPath></text>
      <text><textPath href="#ringInnerB" startOffset="30.5%">SPRING</textPath></text>
    </g>
  </svg>

  <header class="header">
    <div class="brand"><span class="brand-dot"></span><span class="brand-name">Tallowbrook Farm</span></div>
    <h1 class="title">THE WARDANDI SIX SEASONS</h1>
    <div class="tree-art" role="img" aria-label="Illustration of a leafy green tree"></div>
  </header>
  <div class="rule"></div>

  <section class="season birak">
    <h3 class="months">DECEMBER AND JANUARY</h3>
    <h2 class="name">BIRAK</h2>
    <p>Dry and hot long days with warm nights.<br>The low tides are a good time to collect<br>abalone and other shellfish.<br>It is the time foreating blue groper,<br>octopus &amp; oysters.</p>
  </section>

  <section class="season kambarang">
    <h3 class="months">OCTOBER AND<br>NOVEMBER</h3>
    <h2 class="name">KAMBARANG</h2>
    <p>Hot days with nights<br>warming up and winds<br>easing.Lots of baby ducks,<br>emus, possums, kangaroos<br>around. Time to start<br>moving camp<br>towards the<br>coastal areas and<br>make fishing<br>spears.</p>
  </section>

  <section class="season bunuru">
    <h3 class="months">FEBRUARY<br>AND MARCH</h3>
    <h2 class="name">BUNURU</h2>
    <p>Hot days with cooler nights.<br>It is a good time to camp<br>and fish along the<br>west coast for herring,<br>taylor, bream and<br>migrating salmon.</p>
  </section>

  <section class="season djilba">
    <h3 class="months">AUGUST AND<br>SEPTEMBER</h3>
    <h2 class="name">DJILBA</h2>
    <p>Warmer days and cold nights.<br>Time to collect bush fruits<br>and camp in sheltered<br>bays and waterways.<br>Time to hunt for crab,<br>snapper,s quid,<br>marron.</p>
  </section>

  <section class="season djeran">
    <h3 class="months">APRIL<br>AND MAY</h3>
    <h2 class="name">DJERAN</h2>
    <p>Overcast days and the<br>nightsare cooling. It is<br>time to move camp<br>back inland to collect<br>vegetables and<br>catch crabs and fish<br>in the inland<br>estuaries and<br>bays.</p>
  </section>

  <section class="season makuru">
    <h3 class="months">JUNE AND JULY</h3>
    <h2 class="name">MAKURU</h2>
    <p>Cold days and nights - winter rains strong<br>south west winds.  It is time to build strong paper<br>bark mia's. Kangaroo and wallaby are hunted - for<br>eating and to usetheir skins for warmth.<br>Emu's are nesting inland.</p>
  </section>

  <p class="credit">Information provided by Lena Marsh – Wardandi Traditional Owner and owner of Karri Path Tours</p>

  <footer class="footer">
    <div class="photo-left" role="img" aria-label="Photograph looking up at tall karri tree trunks and canopy"></div>
    <address class="contact">
      <b>a</b>: Penfold Rd (Via Lyall Rd), Brookvale<br>
      <b>p</b>: Locked Bag 7, Brookvale WA 6299<br>
      w: www.tallowbrookfarm.com.au &nbsp;<b>e</b>: stay@tallowbrookfarm.com.au<br>
      <b>t</b>:08 9700 4816 &nbsp;<b>m</b>: 0400 517 262
    </address>
    <div class="photo-right" role="img" aria-label="Photograph of a small green frog on red-brown bark among leaves"></div>
  </footer>
</main>
</body>
</html>
```